Corvell Social "is a company that is focused on managing social media platforms.

I need a website design for a social media management company. The owner is a social media influencer in the Denver, Co area. Would like IG and Tik Tok page intergraded into the site. Would like all post from social to go directly to new website. Also put a page link for blog: her is my blog https://www.plumtrove.com/about

Target Market(s)

Any business that needs social media managed or video made for their company.

Coding

Coded - Design and coding required

Requirements
Must have
• Color scheme needs to match logo ; • IG: https://www.instagram.example/plum.trove/ • Clipwave: https://www.tiktok.example/@plum.trove Please add these videos: https://files.example/b-xQ7mLp2Rta
Nice to have
• • https://greyfinstudio.example/ "this a website that i like in the industry"

```html
<!DOCTYPE html>
<html lang="en">
<head>
<meta charset="utf-8">
<title>Corvell Social – Social Media Management</title>
<link href="https://fonts.googleapis.com/css2?family=Montserrat:wght@600;700;800;900&family=Kumbh+Sans:wght@400;500;600;700&display=swap" rel="stylesheet">
<style>
:root{
  --navy:#0b1c3d;
  --navy-deep:#08162f;
  --sand:#e4d6c4;
  --teal:#1a86a6;
  --ink:#1d2430;
  --muted:#4b5563;
  --paper:#f8f8f8;
  --white:#ffffff;
  --red:#d8433e;
  --cobalt:#16398d;
  --gold:#f6b81b;
  --bar:#12799a;
}
*{box-sizing:border-box;margin:0;padding:0}
html,body{width:1200px;height:3757px;overflow:hidden}
body{position:relative;font-family:"Kumbh Sans",sans-serif;color:var(--ink);background:var(--paper)}
.abs{position:absolute}
section,header,footer{position:absolute;left:0;width:1200px}
.heading{font-family:"Montserrat",sans-serif;font-weight:800;letter-spacing:.5px}
.btn{position:absolute;display:flex;align-items:center;justify-content:center;font-size:10px;letter-spacing:.4px;text-transform:uppercase;border:1.5px solid var(--muted);color:var(--ink);background:transparent;white-space:nowrap}

/* wordmark */
.wordmark{position:absolute;color:var(--sand);font-family:"Kumbh Sans",sans-serif;font-weight:500;text-transform:uppercase;white-space:nowrap}

/* hero */
.hero{top:0;height:556px;background:var(--navy)}
.nav{position:absolute;top:29px;left:513px;font-size:9.5px;color:#cfd6e4;text-transform:uppercase;letter-spacing:.3px}
.nav span{position:absolute;white-space:nowrap}
.nav .active{color:var(--teal)}
.hero .touch{left:1035px;top:23px;width:102px;height:28px;border-color:#cfd6e4;color:#e6eaf1;font-size:9.5px}
.hero-title{position:absolute;left:0;width:1200px;text-align:center;color:var(--sand);font-family:"Montserrat",sans-serif;font-weight:900;font-size:54px;line-height:56px;letter-spacing:2px;top:170px}
.hero-sub{position:absolute;left:0;width:1200px;top:288px;text-align:center;color:var(--sand);font-size:29px;letter-spacing:1px}
.hero .cta{border-color:var(--sand);color:var(--sand);font-size:12px;top:348px;height:34px}

/* about */
.about{top:556px;height:522px;background:var(--paper)}
.photo{position:absolute}
.about h2{position:absolute;left:643px;top:126px;color:var(--teal);font-size:31px}
.about p{position:absolute;left:643px;width:380px;font-size:10.2px;line-height:15px;color:var(--muted)}

/* services */
.services{top:1078px;height:720px;background:var(--navy)}
.services h2{position:absolute;top:68px;width:1200px;text-align:center;color:#fff;font-size:29px;letter-spacing:1px}
.card{position:absolute;width:279px;height:244px;background:#fff}
.card .icon{position:absolute;left:24px;top:28px;width:66px;height:66px;border-radius:10px}
.card h3{position:absolute;left:24px;top:116px;font-family:"Montserrat",sans-serif;font-weight:700;font-size:17.5px;color:var(--ink);white-space:nowrap}
.card p{position:absolute;left:24px;top:146px;width:220px;font-size:10.5px;line-height:16px;color:var(--muted)}
.card .btn{left:24px;top:190px;width:91px;height:24px;font-size:9.5px}

/* why */
.why{top:1798px;height:491px;background:var(--paper)}
.why h2{position:absolute;left:156px;top:95px;color:var(--teal);font-size:31px;line-height:31px}
.why .lede{position:absolute;left:156px;top:170px;width:420px;font-size:9.8px;line-height:14px;color:var(--muted)}
.why ul{position:absolute;left:156px;top:216px;list-style:none}
.why li{display:flex;align-items:center;gap:9px;height:28.8px;font-size:13px;color:var(--ink)}
.why .photo-wrap{position:absolute;left:637px;top:87px;width:407px;height:322px}

/* stories */
.stories{top:2289px;height:605px;background:var(--navy)}
.stories h2{position:absolute;top:66px;width:1200px;text-align:center;color:#fff;font-size:29px;letter-spacing:1px}
.story{position:absolute;top:125px;height:350px}
.story h3{position:absolute;left:44px;top:42px;font-family:"Montserrat",sans-serif;font-weight:700;font-size:20px;line-height:24px;color:var(--gold)}
.story p{position:absolute;left:44px;font-size:10.8px;line-height:16px;color:#fff}
.story b{font-weight:500;color:var(--gold)}
.story .arrow{position:absolute;left:44px;top:266px;width:38px;height:36px;border:1px solid rgba(255,255,255,.55);display:flex;align-items:center;justify-content:center}
.stories .view{left:560px;top:511px;width:80px;height:28px;border-color:#cfd6e4;color:#e6eaf1}

/* testimonials */
.testimonials{top:2894px;height:356px;background:var(--paper)}
.testimonials h2{position:absolute;top:64px;width:1225px;text-align:center;color:var(--teal);font-size:29px}
.testimonials blockquote{position:absolute;left:332px;top:128px;width:690px;font-size:16.5px;line-height:24.5px;color:var(--ink)}
.testimonials cite{position:absolute;left:332px;top:264px;font-style:normal;font-size:15px;color:var(--muted)}

/* gallery */
.gallery{top:3250px;height:223px;background:var(--navy-deep)}
.tile{position:absolute;top:17px;width:188px;height:188px}

/* footer */
.footer{top:3473px;height:239px;background:var(--navy)}
.footer h4{position:absolute;font-size:12.5px;font-weight:600;color:var(--teal)}
.footer .line{position:absolute;display:flex;align-items:flex-start;gap:8px;font-size:11px;line-height:14px;color:#fff}
.footer .link{position:absolute;font-size:10.5px;color:#fff}
.bottom{top:3712px;height:45px;background:var(--bar)}
.bottom .copy{position:absolute;left:156px;top:15px;font-size:11px;color:#fff}
.soc{position:absolute;top:14px;width:16px;height:16px}
</style>
</head>
<body>

<header class="hero">
  <div class="wordmark" style="left:61px;top:30px;font-size:15px;letter-spacing:3px">Corvell Social</div>
  <nav class="nav">
    <span class="active" style="left:0;text-decoration:underline">Home</span>
    <span style="left:60px">About Us</span>
    <span style="left:141px">What We Do</span>
    <span style="left:238px">Portfolio</span>
    <span style="left:324px">Careers</span>
    <span style="left:397px">Contact Us</span>
  </nav>
  <a class="btn touch">Get In Touch</a>
  <h1 class="hero-title">ELEVATE YOUR<br>SOCIAL PRESENCE</h1>
  <div class="hero-sub">WITH CORVELL SOCIAL</div>
  <a class="btn cta" style="left:423px;width:210px">Get A Free Consultation</a>
  <a class="btn cta" style="left:646px;width:131px">Learn More</a>
</header>

<section class="about">
  <div class="photo" role="img" aria-label="Two smiling women looking at a phone together" style="left:156px;top:87px;width:316px;height:347px;background:linear-gradient(135deg,#c9b6a3,#7b5a47 55%,#3c2c26)"></div>
  <div class="photo" role="img" aria-label="Video still of hands typing on a laptop, with a play button" style="left:362px;top:189px;width:214px;height:210px;background:linear-gradient(135deg,#d59a4e,#6e5a4c 60%,#2e3238);border:5px solid #fff">
    <svg class="abs" style="left:78px;top:78px" width="46" height="46" viewBox="0 0 46 46"><circle cx="23" cy="23" r="22" fill="#1c2a4e" opacity=".85"/><path d="M18 14 L32 23 L18 32 Z" fill="#e5533a"/></svg>
  </div>
  <h2 class="heading">ABOUT US</h2>
  <p style="top:183px">Imagine Your Company's Snapgrid And Clipwave Alive With Engagement, Capturing New Audiences, And Consistently Driving Measurable Results. This Is The Elevated Standard At Corvell Social, Your Dedicated Social Media Management Partner</p>
  <p style="top:258px">Founded By An Influencer And Content Creator, Corvell Social Brings An Insider's Understanding To Crafting Strategic Narratives, Creating Visually Stunning Content, And Leveraging The Latest Trends To Catapult Your Online Presence. Consider Us Your Dedicated Growth Team Right Here In Denver, Freeing You To Concentrate On What You Do Best.</p>
  <a class="btn" style="left:643px;top:361px;width:108px;height:28px;font-size:9.5px">Explore More</a>
</section>

<section class="services">
  <h2 class="heading">WHAT WE DO</h2>

  <div class="card" style="left:156px;top:126px">
    <div class="icon" role="img" aria-label="Photo app management icon" style="background:#e6f1f6"></div>
    <h3>Snapgrid Management</h3>
    <p>We cultivate compelling profiles and curate dynamic content tailored...</p>
    <a class="btn">Read More</a>
  </div>
  <div class="card" style="left:461px;top:126px">
    <div class="icon" role="img" aria-label="Short video app management icon" style="background:#e6f1f6"></div>
    <h3>Clipwave Management</h3>
    <p>We cultivate compelling profiles and curate dynamic content tailored...</p>
    <a class="btn">Read More</a>
  </div>
  <div class="card" style="left:765px;top:126px">
    <div class="icon" role="img" aria-label="Puzzle pieces strategy icon" style="background:#e4e9f7"></div>
    <h3>Social Media Strategy</h3>
    <p>We cultivate compelling profiles and curate dynamic content tailored...</p>
    <a class="btn">Read More</a>
  </div>
  <div class="card" style="left:156px;top:395px">
    <div class="icon" role="img" aria-label="Document content icon" style="background:#fbe0dc"></div>
    <h3>Content Creation</h3>
    <p>We cultivate compelling profiles and curate dynamic content tailored...</p>
    <a class="btn">Read More</a>
  </div>
  <div class="card" style="left:461px;top:395px">
    <div class="icon" role="img" aria-label="Community group icon" style="background:#ece6f7"></div>
    <h3>Community Management</h3>
    <p>We cultivate compelling profiles and curate dynamic content tailored...</p>
    <a class="btn">Read More</a>
  </div>
  <div class="card" style="left:765px;top:395px">
    <div class="icon" role="img" aria-label="Paid advertising icon" style="background:#fbf0d4"></div>
    <h3>Paid Social Advertising</h3>
    <p>We cultivate compelling profiles and curate dynamic content tailored...</p>
    <a class="btn">Read More</a>
  </div>
</section>

<section class="why">
  <h2 class="heading">WHY CHOOSE<br>CORVELL SOCIAL?</h2>
  <p class="lede">Choosing The Right Social Media Partner Is Crucial For Your Brand's Success. Here's Why Corvell Social Stands Apart As Your Premier Choice In Denver:</p>
  <ul>
    <li><svg width="17" height="17" viewBox="0 0 17 17"><circle cx="8.5" cy="8.5" r="7.5" fill="none" stroke="#4a6fa5" stroke-width="1.3"/><path d="M5 8.5h7M9.5 6l2.5 2.5-2.5 2.5" fill="none" stroke="#4a6fa5" stroke-width="1.3"/></svg>Insider Expertise From An Established Influencer.</li>
    <li><svg width="17" height="17" viewBox="0 0 17 17"><circle cx="8.5" cy="8.5" r="7.5" fill="none" stroke="#4a6fa5" stroke-width="1.3"/><path d="M5 8.5h7M9.5 6l2.5 2.5-2.5 2.5" fill="none" stroke="#4a6fa5" stroke-width="1.3"/></svg>Unrivaled Platform Mastery.</li>
    <li><svg width="17" height="17" viewBox="0 0 17 17"><circle cx="8.5" cy="8.5" r="7.5" fill="none" stroke="#4a6fa5" stroke-width="1.3"/><path d="M5 8.5h7M9.5 6l2.5 2.5-2.5 2.5" fill="none" stroke="#4a6fa5" stroke-width="1.3"/></svg>Strategic, Results-Driven Approach:</li>
    <li><svg width="17" height="17" viewBox="0 0 17 17"><circle cx="8.5" cy="8.5" r="7.5" fill="none" stroke="#4a6fa5" stroke-width="1.3"/><path d="M5 8.5h7M9.5 6l2.5 2.5-2.5 2.5" fill="none" stroke="#4a6fa5" stroke-width="1.3"/></svg>Dedicated Local Partnership.</li>
    <li><svg width="17" height="17" viewBox="0 0 17 17"><circle cx="8.5" cy="8.5" r="7.5" fill="none" stroke="#4a6fa5" stroke-width="1.3"/><path d="M5 8.5h7M9.5 6l2.5 2.5-2.5 2.5" fill="none" stroke="#4a6fa5" stroke-width="1.3"/></svg>Bespoke &amp; Personalized Service.</li>
  </ul>
  <a class="btn" style="left:156px;top:374px;width:108px;height:28px;font-size:9.5px">Explore More</a>
  <div class="abs" style="left:685px;top:82px;width:312px;height:5px;background:var(--bar)"></div>
  <div class="abs" style="left:685px;top:409px;width:312px;height:5px;background:var(--bar)"></div>
  <div class="photo-wrap" role="img" aria-label="Woman smiling at her phone surrounded by review bubbles and reaction icons" style="background:linear-gradient(160deg,#7d8f6a,#b9b2a0 50%,#6a7f9a)"></div>
</section>

<section class="stories">
  <h2 class="heading">CLIENT SUCCESS STORIES</h2>

  <div class="story" style="left:156px;width:663px;background:var(--red)">
    <h3>Larkspur Burgers<br>(Rocky Mountain Region)</h3>
    <p style="top:110px">Driving Local Engagement Through Feel-Good Content</p>
    <p style="top:141px;width:370px"><b>Visual:</b> A phone image, held vertically, showcasing a beautifully shot short clip or Clipwave-style video for Larkspur Burgers. (provide to Theo)</p>
    <p style="top:189px;width:370px"><b>Description:</b> Our collaboration with Larkspur Burgers of the Rocky Mountain Region focused on creating relatable and visually appealing content that tapped into...</p>
    <div class="arrow"><svg width="14" height="10" viewBox="0 0 14 10"><path d="M1 5h12M9 1l4 4-4 4" fill="none" stroke="#fff" stroke-width="1.3"/></svg></div>
    <div class="abs" style="left:477px;top:18px;width:150px;height:313px;border:3px solid #111;border-radius:22px;background:#fff;padding:5px">
      <div role="img" aria-label="Vertical short video of a restaurant storefront" style="width:100%;height:100%;border-radius:16px;background:linear-gradient(180deg,#e9e2dc,#b4a9a2 60%,#d6cbc3);position:relative">
        <div style="position:absolute;left:44px;top:110px;width:48px;height:48px;background:#d5222a"></div>
        <div style="position:absolute;left:0;width:100%;top:166px;text-align:center;color:#1d2430;font-family:'Kumbh Sans',sans-serif;font-size:11px;font-weight:700">Larkspur Burgers</div>
      </div>
      <div style="position:absolute;left:52px;top:6px;width:40px;height:10px;border-radius:6px;background:#111"></div>
    </div>
  </div>

  <div class="story" style="left:838px;width:362px;background:var(--cobalt);overflow:hidden">
    <h3>RTSA</h3>
    <p style="top:85px;white-space:nowrap">Communicating Vital Messages with Widespread Impact</p>
    <p style="top:116px;width:360px"><b>Visual:</b> A phone image, held vertically, playing a compelling short video or clip. Use Drive Clear Video (provide to Theo)</p>
    <p style="top:164px;width:360px"><b>Description:</b> For RTSA, our objective was to transform essential public safety messages into highly digestible and widely shared content. We developed creative narratives around impaired driving prevention, like the "Drive Clear...</p>
    <div class="arrow"><svg width="14" height="10" viewBox="0 0 14 10"><path d="M1 5h12M9 1l4 4-4 4" fill="none" stroke="#fff" stroke-width="1.3"/></svg></div>
  </div>

  <a class="btn view">View All</a>
</section>

<section class="testimonials">
  <h2 class="heading">TESTIMONIALS</h2>
  <svg class="abs" style="left:204px;top:172px" width="74" height="56" viewBox="0 0 74 56"><path d="M0 0h32v30c0 14-8 24-20 26l-2-7c7-2 10-8 10-15H0Z" fill="#1a86a6"/><path d="M40 0h32v30c0 14-8 24-20 26l-2-7c7-2 10-8 10-15H40Z" fill="#1a86a6"/></svg>
  <blockquote>Lorem Ipsum Is Simply Dummy Text Of The Printing And Typesetting Industry. Lorem Ipsum Has Been The Industry's Standard Dummy Text Ever Since The 1500s, When An Unknown Printer Took A Galley Of Type And Scrambled It To Make A Type Specimen Book. It Has Survived Not Only Five Centuries, But Also The Leap Into Electronic Typesetting, Remaining Essentially Unchanged.</blockquote>
  <cite>- Dana M.</cite>
  <svg class="abs" style="left:952px;top:270px" width="16" height="12" viewBox="0 0 16 12"><path d="M15 6H1M5 2L1 6l4 4" fill="none" stroke="#4b5563" stroke-width="1.4"/></svg>
  <svg class="abs" style="left:981px;top:270px" width="16" height="12" viewBox="0 0 16 12"><path d="M1 6h14M11 2l4 4-4 4" fill="none" stroke="#1aa0c4" stroke-width="1.4"/></svg>
</section>

<section class="gallery">
  <div class="tile" role="img" aria-label="Social post: drink being poured" style="left:22px;background:linear-gradient(135deg,#8a5a2c,#e2a640 60%,#c3501f)"></div>
  <div class="tile" role="img" aria-label="Social video: restaurant interior" style="left:216px;background:linear-gradient(135deg,#3a2a24,#6d5a4c 55%,#2a2522)">
    <svg class="abs" style="left:64px;top:64px" width="60" height="60" viewBox="0 0 60 60"><circle cx="30" cy="30" r="29" fill="#1c2a4e" opacity=".85"/><path d="M24 19 L41 30 L24 41 Z" fill="#fff"/></svg>
  </div>
  <div class="tile" role="img" aria-label="Social post: plate of green peppers" style="left:410px;background:linear-gradient(135deg,#5c6b23,#a4a23c 55%,#40401c)"></div>
  <div class="tile" role="img" aria-label="Social post: boxed meals on a table" style="left:603px;background:linear-gradient(135deg,#2a2420,#6a4e32 55%,#c59a3c)"></div>
  <div class="tile" role="img" aria-label="Social post: man holding an iced coffee" style="left:797px;background:linear-gradient(135deg,#4a3528,#a87a58 50%,#d8632a)"></div>
  <div class="tile" role="img" aria-label="Social post: guests at a lounge" style="left:991px;background:linear-gradient(135deg,#3c3a40,#8b8188 55%,#c9c2c0)"></div>
</section>

<footer class="footer">
  <div class="wordmark" style="left:156px;top:108px;font-size:17px;letter-spacing:4px">Corvell Social</div>

  <h4 style="left:420px;top:50px">Contact Us</h4>
  <div class="line" style="left:420px;top:80px"><svg width="11" height="11" viewBox="0 0 12 12"><path d="M2 1l2.5 0 1 3-1.5 1c.8 1.5 1.5 2.2 3 3l1-1.5 3 1V10c0 .6-.5 1-1 1C5 11 1 7 1 2c0-.5.4-1 1-1Z" fill="#1a86a6"/></svg>(720) 555-0148</div>
  <div class="line" style="left:420px;top:108px"><svg width="11" height="11" viewBox="0 0 12 12"><rect x="1" y="4" width="10" height="7" rx="1" fill="#1a86a6"/><rect x="3" y="1" width="6" height="3" fill="#1a86a6"/></svg>(720) 555-0193</div>
  <div class="line" style="left:420px;top:136px"><svg width="11" height="11" viewBox="0 0 12 12"><rect x="1" y="2.5" width="10" height="7.5" fill="#1a86a6"/><path d="M1 3l5 4 5-4" fill="none" stroke="#0b1c3d" stroke-width="1"/></svg>hello@corvellmail.example</div>
  <div class="line" style="left:420px;top:162px"><svg width="11" height="14" viewBox="0 0 12 15"><path d="M6 0C3 0 1 2.2 1 5c0 4 5 10 5 10s5-6 5-10c0-2.8-2-5-5-5Z" fill="#1a86a6"/><circle cx="6" cy="5" r="2" fill="#0b1c3d"/></svg>4120 Alder Lane,<br>Lakewood, CO 80226&nbsp; USA</div>

  <h4 style="left:647px;top:50px">Quick Inquiry</h4>
  <div class="link" style="left:647px;top:72px;color:var(--teal);text-decoration:underline">Home</div>
  <div class="link" style="left:647px;top:93px">About Us</div>
  <div class="link" style="left:647px;top:115px">What We Do</div>
  <div class="link" style="left:647px;top:136px">Portfolio</div>
  <div class="link" style="left:647px;top:158px">Careers</div>
  <div class="link" style="left:647px;top:179px">Contact Us</div>

  <svg class="abs" style="left:795px;top:47px" width="34" height="30" viewBox="0 0 34 30"><path d="M2 11L17 2l15 9v17H2Z" fill="none" stroke="#1a86a6" stroke-width="2"/><path d="M2 11l15 10 15-10" fill="none" stroke="#1a86a6" stroke-width="2"/></svg>
  <h4 style="left:842px;top:51px;line-height:14px">Subscribe To Our<br>Newsletter</h4>
  <div class="abs" style="left:795px;top:95px;width:249px;height:30px;background:#fff;display:flex;align-items:center;justify-content:space-between;padding:0 10px;font-size:9.5px;color:#8a93a3">Enter Email<svg width="14" height="13" viewBox="0 0 14 13"><path d="M0 0l14 6.5L0 13l2-6.5Z" fill="#0b1c3d"/></svg></div>
  <h4 style="left:795px;top:142px">Opening Hours:</h4>
  <div class="link" style="left:795px;top:164px;font-size:9.8px">Mon-Thurs 9:00 am - 4:00 pm</div>
  <div class="link" style="left:795px;top:180px;font-size:9.8px">Fri 9:00 am - 12:30 pm</div>
</footer>

<footer class="bottom">
  <div class="copy">© 2025 Corvell Social. All Rights Reserved.</div>
  <div class="soc" role="img" aria-label="Social link" style="left:964px;background:#0b1c3d;border-radius:2px"></div>
  <div class="soc" role="img" aria-label="Social link" style="left:992px;background:#0b1c3d;border-radius:2px"></div>
  <div class="soc" role="img" aria-label="Social link" style="left:1020px;top:11px;width:22px;height:22px;background:#0b1c3d;border-radius:50%"></div>
</footer>

</body>
</html>
```